Business cards design for T38 (Разработка визитных карточек)

We would like to get design of our business cards loosely based on our website design [url removed, login to view]

logo in vector is atteched

There should be following info to be present on business card:
Martin Colvey
CEO
T38
+7 (222) 222-22-22
+7 (222) 222-22-22
colvey@tessarine-mail.ru
222222, Moscow, Ulitsa Tikhvoronskaya, 7B

```html
<!DOCTYPE html>
<html lang="en">
<head>
<meta charset="utf-8">
<title>T38 — Business Cards</title>
<link rel="stylesheet" href="https://fonts.googleapis.com/css2?family=Ubuntu:wght@300;400;500;700&display=swap">
<style>
  :root {
    --bg-top: #2a2a2a;
    --bg-bottom: #070707;
    --paper: #f3f3f3;
    --paper-edge: #e2e2e2;
    --brand-red: #e0262b;
    --ink: #3a3a3a;
    --ink-soft: #5b5b5b;
    --band-dark: #3b3b3b;
    --white: #ffffff;
  }
  * { box-sizing: border-box; margin: 0; padding: 0; }
  html, body {
    width: 1200px; height: 872px; overflow: hidden;
  }
  body {
    background: radial-gradient(ellipse at 50% 35%, var(--bg-top), var(--bg-bottom) 75%);
    font-family: "Ubuntu", "Segoe UI", sans-serif;
    display: flex; align-items: center; justify-content: center; gap: 44px;
  }
  .card {
    position: relative;
    width: 540px; height: 310px;
    background: linear-gradient(160deg, var(--white), var(--paper) 60%, var(--paper-edge));
    box-shadow: 0 18px 40px rgba(0,0,0,.55);
    overflow: hidden;
  }

  /* front */
  .contact-row {
    position: absolute; top: 22px; left: 30px; right: 30px;
    display: flex; justify-content: space-between;
    font-size: 10.5px; line-height: 1.45; color: var(--ink-soft); font-weight: 400;
  }
  .contact-row .email { align-self: flex-end; }
  .icon-band {
    position: absolute; top: 72px; left: 0; right: 0; height: 12px;
    background: var(--band-dark);
  }
  .icon-badge {
    position: absolute; top: 63px; width: 30px; height: 30px;
  }
  .icon-badge.home { left: 66px; }
  .icon-badge.phone { left: 257px; }
  .icon-badge.mail { left: 444px; }
  .rule-red {
    position: absolute; left: 0; right: 0; height: 1.5px; background: var(--brand-red);
  }
  .rule-red.upper { top: 114px; }
  .rule-red.lower { top: 216px; }
  .brand-name {
    position: absolute; left: 0; right: 0;
    text-align: center; color: var(--brand-red);
    font-weight: 700; letter-spacing: 2px;
  }
  .front .brand-name { top: 116px; font-size: 86px; line-height: 100px; }
  .person {
    position: absolute; right: 52px; top: 230px; text-align: right;
  }
  .person-name {
    font-size: 25px; font-weight: 300; letter-spacing: 1px; color: var(--ink);
    text-transform: uppercase; line-height: 1.1;
  }
  .person-name .surname { color: var(--brand-red); font-weight: 400; }
  .person-role {
    font-size: 11px; color: var(--ink-soft); letter-spacing: 1px; margin-top: 3px;
  }
  .person-mark {
    position: absolute; right: 36px; top: 233px; width: 6px; height: 34px;
    background: var(--brand-red);
  }

  /* back */
  .back .brand-name { top: 58px; font-size: 96px; line-height: 110px; }
  .axis-line {
    position: absolute; left: 0; right: 0; top: 206px; height: 1.5px; background: var(--band-dark);
  }
  .web-band {
    position: absolute; left: 70px; right: 70px; top: 182px; height: 48px;
    background: var(--brand-red);
    display: flex; align-items: center; justify-content: center;
    color: var(--white); font-size: 18px; font-weight: 500; letter-spacing: .5px;
  }
</style>
</head>
<body>

  <section class="card front" aria-label="Business card front">
    <div class="contact-row">
      <p class="address">222222, Moscow,<br>Ulitsa Tikhvoronskaya, 7B</p>
      <p class="phones">+7 (222) 222-22-22<br>+7 (222) 222-22-22</p>
      <p class="email">colvey@tessarine-mail.ru</p>
    </div>

    <div class="icon-band"></div>
    <svg class="icon-badge home" viewBox="0 0 30 30" aria-label="Address">
      <circle cx="15" cy="15" r="15" fill="var(--brand-red)"/>
      <path d="M8 15 L15 8.5 L22 15 M10.5 13 V21.5 H19.5 V13" fill="none" stroke="#fff" stroke-width="2" stroke-linejoin="round"/>
    </svg>
    <svg class="icon-badge phone" viewBox="0 0 30 30" aria-label="Phone">
      <circle cx="15" cy="15" r="15" fill="var(--brand-red)"/>
      <path d="M8 11 Q8 9 11 9 H19 Q22 9 22 11 V12.5 H18.5 V11.5 H11.5 V12.5 H8 Z M10.5 14 H19.5 L21 21.5 H9 Z" fill="#fff"/>
      <circle cx="15" cy="17.5" r="2" fill="var(--brand-red)"/>
    </svg>
    <svg class="icon-badge mail" viewBox="0 0 30 30" aria-label="Email">
      <circle cx="15" cy="15" r="15" fill="var(--brand-red)"/>
      <rect x="8" y="10" width="14" height="10" fill="#fff"/>
      <path d="M8 10 L15 16 L22 10" fill="none" stroke="var(--brand-red)" stroke-width="1.5"/>
    </svg>

    <div class="rule-red upper"></div>
    <div class="brand-name">T38</div>
    <div class="rule-red lower"></div>

    <div class="person">
      <p class="person-name">Martin <span class="surname">Colvey</span></p>
      <p class="person-role">CEO</p>
    </div>
    <div class="person-mark"></div>
  </section>

  <section class="card back" aria-label="Business card back">
    <div class="brand-name">T38</div>
    <div class="axis-line"></div>
    <div class="web-band">www.t38tessarine.ru</div>
  </section>

</body>
</html>
```